Bar Soap Packaging Design for Facial Cleansing Bar

Hi,

I have a business that sells soaps, lotions, and other skincare products and I'd like a design for a box for a bar soap that is primarily for women.

The name of the brand is 'Velmo Shea Blend' and the brand is all about renewal and rejuvenation.

I've attached my logo and photos of packaging for bar soaps that are best sellers in my market.

The box is 3 inches x 2 inches and has a white background.

Info to go on the box:

1. Brand name: Velmo Shea Blend

2. [To go below brand name]: Facial Bar

3. Address: Distributed by Haverlin Trading Ltd, 47 Marlow St., Kingston, Jamaica W.I.

4. Contact: tamsin@velmosheablend.example

5. Net Weight: 3.6 oz /102g

6. Ingredients: glycerine, palmitic acid, sodium chloride, water, cocoa butter, fragrance, AOS, EDTA, vitamin E, color.

7. Directions: Wet face. Lather soap in hands. Gently massage lather onto face and neck. Rinse with water and pat dry with a towel. For day, follow with a sunscreen. At night, follow with a serum and/or moisturizer.

8. Please put a circle somewhere on the front with the words: 'Boosts Hydration 100%' in the circle

9. Batch Code: [please leave space beside 'Batch Code' blank]

10. Best Before: April 2019

11. Please put somewhere on the the front: For Younger Looking Skin

12. Please put somewhere on the front: with Real Cocoa Butter and Vitamin E

Thank you,
Tamsin

Target Market(s)

Women 27 to 60 who are looking for anti-age skincare products that'll make them look younger

Industry/Entity Type

Business

Font styles to use
Sans Serif

Colors

Designer to choose colors to be used in the design.

Requirements
Must have
• The info that I've asked for in the brief
Nice to have
• A design similar to the packaging for the brand of soap 'Odra' that I've attached.
Should not have
• Not sure...

```html
<!DOCTYPE html>
<html lang="en">
<head>
<meta charset="utf-8">
<title>Velmo Shea Blend – Facial Bar Carton Dieline</title>
<link rel="stylesheet" href="https://fonts.googleapis.com/css2?family=Alegreya:wght@400;700&display=swap">
<style>
  :root {
    --bg: #eef7fb;
    --paper: #ffffff;
    --cut-line: #a9b3ba;
    --tab-blue: #1aa3e0;
    --flap-blue: #45c5f6;
    --navy: #2a2a7c;
    --plum: #8b3f98;
    --product-ink: #3a2418;
    --label-blue: #1a9fdc;
    --ink: #1e1e24;
    --seal-ring: #c9a24a;
  }
  html, body { margin: 0; padding: 0; overflow: hidden; }
  body { width: 1200px; height: 1200px; background: var(--bg); }
  .dieline { display: block; width: 1200px; height: 1200px; }
  .panel { fill: var(--paper); stroke: var(--cut-line); stroke-width: 1.2; }
  .flap-blue { fill: var(--flap-blue); stroke: var(--cut-line); stroke-width: 1.2; }
  .tagline-tab { fill: var(--tab-blue); }
  .tagline { font-family: "Alegreya", serif; font-size: 15px; fill: #fff; letter-spacing: .2px; }
  .brand-name { font-family: "Alegreya", serif; font-weight: 400; fill: var(--navy); }
  .product-box { fill: #fff; stroke: var(--plum); stroke-width: 2.4; }
  .product-name { font-family: "Alegreya", serif; font-weight: 700; fill: var(--product-ink); letter-spacing: .5px; }
  .claim { font-family: "Alegreya", serif; fill: var(--plum); }
  .info { font-family: "Alegreya", serif; font-size: 11.6px; fill: var(--ink); }
  .info-label { fill: var(--label-blue); font-weight: 700; }
  .net-weight { font-family: "Alegreya", serif; font-size: 12px; font-weight: 700; fill: var(--ink); }
  .seal { fill: var(--navy); stroke: var(--seal-ring); stroke-width: 3; }
  .seal-text { font-family: "Alegreya", serif; font-weight: 700; fill: #fff; text-anchor: middle; }
</style>
</head>
<body>
<svg class="dieline" viewBox="0 0 1500 1500" xmlns="http://www.w3.org/2000/svg">
  <defs>
    <linearGradient id="wave-band" x1="0" y1="0" x2="0" y2="1">
      <stop offset="0" stop-color="#ffffff" stop-opacity="0"/>
      <stop offset=".35" stop-color="#9fe3fb"/>
      <stop offset=".7" stop-color="#3cbcf0"/>
      <stop offset="1" stop-color="#1b8fd8"/>
    </linearGradient>
    <linearGradient id="splash" x1="0" y1="0" x2="0" y2="1">
      <stop offset="0" stop-color="#ffffff" stop-opacity="0"/>
      <stop offset=".5" stop-color="#7cc9ee"/>
      <stop offset="1" stop-color="#1f6fc0"/>
    </linearGradient>
    <radialGradient id="oil-drop" cx=".4" cy=".6" r=".6">
      <stop offset="0" stop-color="#fff1b8"/>
      <stop offset=".6" stop-color="#d9a93a"/>
      <stop offset="1" stop-color="#8f6418"/>
    </radialGradient>
  </defs>

  <rect width="1500" height="1500" fill="var(--bg)"/>

  <g class="carton" transform="translate(0 350)">
    <!-- glue flap -->
    <path class="panel" d="M108 226 L72 230 Q65 231 65 240 L65 564 Q65 572 72 572 L108 575 Z"/>

    <!-- side flaps -->
    <path class="panel" d="M633 226 L633 192 Q633 184 642 184 L754 184 Q763 184 763 192 L763 226 Z"/>
    <path class="panel" d="M633 575 L633 610 Q633 618 642 618 L754 618 Q763 618 763 610 L763 575 Z"/>
    <path class="panel" d="M1287 226 L1287 192 Q1287 182 1297 182 L1408 182 Q1418 182 1418 192 L1418 226 Z"/>
    <path class="panel" d="M1287 575 L1287 610 Q1287 618 1297 618 L1408 618 Q1418 618 1418 610 L1418 575 Z"/>

    <!-- top lid with tuck -->
    <path class="panel" d="M765 226 L765 95 L1285 95 L1285 226 Z"/>
    <path class="panel" d="M765 95 L765 60 Q765 50 777 50 L1273 50 Q1285 50 1285 60 L1285 95 Z"/>

    <!-- bottom blue flaps -->
    <rect class="flap-blue" x="108" y="575" width="525" height="130"/>
    <path class="flap-blue" d="M113 705 L630 705 L630 750 L121 750 Q113 750 113 742 Z"/>

    <!-- main strip -->
    <rect class="panel" x="108" y="226" width="1310" height="349"/>

    <!-- water wave band across all panels -->
    <path role="img" aria-label="Flowing blue water waves" fill="url(#wave-band)"
          d="M108 440 C400 420 620 470 900 430 C1120 400 1300 440 1418 420 L1418 575 L108 575 Z"/>

    <!-- FRONT PANEL -->
    <g class="front-panel">
      <rect class="tagline-tab" x="108" y="226" width="247" height="40"/>
      <text class="tagline" x="118" y="252">• FOR YOUNGER LOOKING SKIN</text>

      <rect role="img" aria-label="Golden vitamin E oil drop with a water splash" x="115" y="280" width="235" height="295" rx="6" fill="url(#splash)"/>
      <ellipse role="img" aria-label="Golden vitamin E oil drop" cx="228" cy="370" rx="42" ry="55" fill="url(#oil-drop)"/>

      <text class="brand-name" x="388" y="318" font-size="60">Velmo</text>
      <text class="brand-name" x="390" y="356" font-size="32">Shea Blend</text>

      <rect class="product-box" x="388" y="370" width="203" height="34" rx="5"/>
      <text class="product-name" x="489.5" y="394" font-size="22" text-anchor="middle">FACIAL BAR</text>

      <text class="claim" x="590" y="427" font-size="21" text-anchor="end">With Real Cocoa Butter</text>
      <text class="claim" x="590" y="451" font-size="21" text-anchor="end">and Vitamin E</text>

      <g class="hydration-seal">
        <circle class="seal" cx="550" cy="512" r="41"/>
        <text class="seal-text" x="550" y="500" font-size="11">BOOSTS</text>
        <text class="seal-text" x="550" y="515" font-size="11">HYDRATION</text>
        <text class="seal-text" x="550" y="535" font-size="17">100%</text>
      </g>
    </g>

    <!-- SIDE PANEL -->
    <g class="hydration-seal">
      <circle class="seal" cx="698" cy="295" r="42"/>
      <text class="seal-text" x="698" y="283" font-size="11">BOOSTS</text>
      <text class="seal-text" x="698" y="298" font-size="11">HYDRATION</text>
      <text class="seal-text" x="698" y="318" font-size="17">100%</text>
    </g>

    <!-- LID upside-down brand -->
    <text class="brand-name" x="1028" y="160" font-size="26" text-anchor="middle" transform="rotate(180 1028 152)">Velmo Shea Blend</text>

    <!-- BACK PANEL -->
    <g class="back-panel">
      <rect class="tagline-tab" x="763" y="226" width="246" height="40"/>
      <text class="tagline" x="782" y="251">• FOR YOUNGER LOOKING SKIN</text>

      <text class="info" x="787" y="291"><tspan class="info-label">Ingredients:</tspan> glycerine, palmitic acid, sodium chloride, water,</text>
      <text class="info" x="787" y="306">cocoa butter, fragrance, AOS, EDTA, vitamin E, color.</text>

      <text class="info" x="787" y="328"><tspan class="info-label">Directions:</tspan> Wet face. Lather soap in hands. Gently massage</text>
      <text class="info" x="787" y="343">lather onto face and neck. Rinse with water and pat dry with</text>
      <text class="info" x="787" y="358">a towel. For day, follow with a sunscreen. At night, follow with</text>
      <text class="info" x="787" y="373">a serum and/or moisturizer.</text>

      <text class="info info-label" x="787" y="390">Address:</text>
      <text class="info" x="787" y="405">Distributed by Haverlin Trading Ltd, 47 Marlow St., Kingston,</text>
      <text class="info" x="787" y="420">Jamaica W.I.</text>

      <g class="email-icon" fill="none" stroke="var(--label-blue)" stroke-width="1.6">
        <rect x="788" y="430" width="40" height="18" rx="2"/>
        <path d="M788 431 L808 442 L828 431"/>
      </g>
      <text class="info" x="836" y="445">tamsin@velmosheablend.example</text>

      <text class="info info-label" x="787" y="469">Batch Code:</text>
      <text class="info" x="787" y="489"><tspan class="info-label">Best Before:</tspan> April 2019</text>

      <text class="brand-name" x="1264" y="312" font-size="42" text-anchor="end">Velmo</text>
      <text class="brand-name" x="1264" y="338" font-size="22" text-anchor="end">Shea Blend</text>

      <rect class="product-box" x="1126" y="347" width="139" height="24" rx="4" stroke-width="1.8"/>
      <text class="product-name" x="1195.5" y="365" font-size="16" text-anchor="middle">FACIAL BAR</text>

      <text class="claim" x="1264" y="386" font-size="14" text-anchor="end">With Real Cocoa Butter</text>
      <text class="claim" x="1264" y="402" font-size="14" text-anchor="end">and Vitamin E</text>
      <text class="net-weight" x="1264" y="418" text-anchor="end">Net Weight: 3.6 oz /102g</text>

      <ellipse role="img" aria-label="Golden vitamin E oil drop" cx="1205" cy="492" rx="29" ry="38" fill="url(#oil-drop)"/>
    </g>
  </g>
</svg>
</body>
</html>
```